Business Card Design Project

Keep it simple , using logo and colors that compliment. Logo on one side with complimentary back ground color. Other side, personal info with possible complimentary design/colors

Target Market(s)

we are a non for profit that will be seeking donations . Both monetary and in kind

Industry/Entity Type

Business

Font styles to use
Sans Serif

Colors

Designer to choose colors to be used in the design.

```html
<!DOCTYPE html>
<html lang="en">
<head>
<meta charset="utf-8">
<title>Lift Together – Business Card</title>
<link href="https://fonts.googleapis.com/css2?family=Lato:wght@300;400;700;900&display=swap" rel="stylesheet">
<style>
  :root {
    --navy: #1f2547;
    --yellow: #e9dc10;
    --white: #ffffff;
    --paper: #f4f4f4;
    --backdrop: #3a3a3a;
    --text-light: #e6e8f0;
  }
  * { box-sizing: border-box; margin: 0; padding: 0; }
  html, body { width: 1200px; height: 900px; overflow: hidden; }
  body {
    background: var(--backdrop);
    font-family: "Lato", Arial, sans-serif;
    position: relative;
  }
  .card {
    position: absolute;
    width: 560px;
    height: 320px;
    border-radius: 22px;
    overflow: hidden;
    background: var(--white);
    box-shadow: 0 10px 30px rgba(0,0,0,.45);
  }
  .card--front { left: 60px; top: 70px; }
  .card--back { left: 580px; top: 500px; }

  /* Front */
  .front-band {
    position: absolute; left: 0; right: 0; bottom: 0; height: 92px;
    background: var(--navy);
    display: flex; align-items: center; justify-content: center;
  }
  .front-rules {
    position: absolute; left: 0; right: 0; bottom: 92px; height: 16px;
    background: repeating-linear-gradient(to bottom, var(--navy) 0 3px, var(--white) 3px 6px);
  }
  .tagline {
    color: var(--yellow);
    font-weight: 700;
    font-size: 15px;
    letter-spacing: 4px;
    text-transform: uppercase;
  }
  .brand-mark {
    position: absolute;
    border-radius: 50%;
    background: var(--navy);
    display: flex; align-items: center; justify-content: center;
    text-align: center;
  }
  .brand-name {
    color: var(--yellow);
    font-weight: 300;
    line-height: 1.05;
  }
  .card--front .brand-mark { width: 178px; height: 178px; left: 186px; top: 16px; }
  .card--front .brand-name { font-size: 30px; }

  /* Back */
  .back-panel {
    position: absolute; top: 0; right: 0; bottom: 0; width: 312px;
    background: var(--navy);
    padding: 34px 20px 0 44px;
    color: var(--text-light);
  }
  .back-rules {
    position: absolute; top: 0; bottom: 0; left: 230px; width: 18px;
    background: repeating-linear-gradient(to right, var(--navy) 0 3px, var(--white) 3px 6px);
  }
  .card--back .brand-mark { width: 200px; height: 200px; left: 18px; top: 60px; }
  .card--back .brand-name { font-size: 34px; }
  .person-name { font-weight: 900; font-size: 19px; color: var(--white); letter-spacing: .3px; }
  .person-title { font-weight: 900; font-size: 13px; color: var(--white); margin: 2px 0 0 14px; letter-spacing: .3px; }
  .contact-list { list-style: none; margin-top: 78px; }
  .contact-list li {
    display: flex; align-items: center; gap: 8px;
    font-size: 14.5px; line-height: 1; margin-bottom: 12px;
  }
  .contact-list svg { width: 14px; height: 14px; flex: none; }
</style>
</head>
<body>

<section class="card card--front" aria-label="Card front">
  <div class="brand-mark"><span class="brand-name">Lift<br>Together</span></div>
  <div class="front-rules"></div>
  <div class="front-band"><p class="tagline">Your slogan/ tagline here</p></div>
</section>

<section class="card card--back" aria-label="Card back">
  <div class="brand-mark"><span class="brand-name">Lift<br>Together</span></div>
  <div class="back-rules"></div>
  <div class="back-panel">
    <h1 class="person-name">DANIEL MARSH</h1>
    <p class="person-title">MANAGING DIRECTOR</p>
    <ul class="contact-list">
      <li>
        <svg viewBox="0 0 16 16" aria-hidden="true"><path fill="currentColor" d="M3 2h3l1 3-2 1.5a9 9 0 0 0 4.5 4.5L11 9l3 1v3a1 1 0 0 1-1 1A12 12 0 0 1 2 3a1 1 0 0 1 1-1z"/></svg>
        +61 400 123 456
      </li>
      <li>
        <svg viewBox="0 0 16 16" aria-hidden="true"><rect x="1.5" y="3.5" width="13" height="9" fill="none" stroke="currentColor" stroke-width="1.4"/><path d="M1.5 3.5 8 9l6.5-5.5" fill="none" stroke="currentColor" stroke-width="1.4"/></svg>
        daniel@brightgive.org.au
      </li>
      <li>
        <svg viewBox="0 0 16 16" aria-hidden="true"><g fill="none" stroke="currentColor" stroke-width="1.6"><rect x="1.5" y="7" width="7" height="4" rx="2" transform="rotate(-45 5 9)"/><rect x="7.5" y="5" width="7" height="4" rx="2" transform="rotate(-45 11 7)"/></g></svg>
        www.brightgive.org.au
      </li>
      <li>
        <svg viewBox="0 0 16 16" aria-hidden="true"><circle cx="8" cy="8" r="4" fill="currentColor"/></svg>
        @brightgive
      </li>
    </ul>
  </div>
</section>

</body>
</html>
```